Marketing Flyer for Coaching Company

Need a marketing flyer I can use based off of my website Quillmoorcoaching.com. Quick Summary of me include "over 40,000 hours of leadership and coaching experience" Talking about the three services offered. Career and life coaching / Steady Oak Callback / Fractional Sales Leadership. I would love to use the colors from the logo. I do not want pricing included.

Target Market(s)

Therapist Offices and other professional treatment centers

Industry/Entity Type

Coaching

Other font styles liked:
• Hero Light Regular

Colors
0054AA
0677BA
7BADD7
CADEEF
E8F1F8
0094D4
00A9DD
6FCCEA
C7EBF8
E9F6FB
00AB8E
00BBA5
67D7C9
C6EFE9
E9F9F6
59FF00
82FF00
B8FF75
E3FFCB
F4FFEA
FFF300
FFF600
FEFA6F
FFFEC7
FFFEE8
EB3D1F
EC4F4E
F09395
F8D3D4
FCEDEE
E54698
E96AAD
F1A4CE
F9D9EA
FCEFF6
A7469A
B969AE
D3A5CF
EDDBEB
F8F0F9
6B429C
8869AF
B7A5CE
E3DAEB
F3F0F8

Requirements
Must have
• Logo "over 40,000 hours of leadership and coaching experience" Talking about the three services offered. Career and life coaching / Steady Oak Callback / Fractional Sales Leadership. I would love to use the colors from the logo. Contact info
Nice to have
• Color Pallet based off of logo pallet id's are in the attachments
Should not have
• Pricing

```html
<!DOCTYPE html>
<html lang="en">
<head>
<meta charset="utf-8">
<title>Quillmoor Coaching Flyer</title>
<link href="https://fonts.googleapis.com/css2?family=Lexend:wght@400;500;600&family=Poppins:wght@400;600&display=swap" rel="stylesheet">
<style>
:root{
  --navy:#0b0a3d;
  --plum:#5a0a3a;
  --royal:#2a3f9e;
  --green:#4f9c14;
  --lime:#9acd32;
  --yellow:#e6ef4c;
  --purple:#8e2a8e;
  --ink:#151515;
  --white:#ffffff;
}
*{margin:0;padding:0;box-sizing:border-box}
html,body{width:1017px;height:1200px;overflow:hidden;background:var(--white)}
.flyer{position:relative;width:1017px;height:1200px;overflow:hidden;font-family:"Poppins",sans-serif;color:var(--ink)}
.abs{position:absolute}

.brand{left:51px;top:60px;width:310px;text-align:center}
.brand-dot{width:58px;height:58px;border-radius:50%;background:var(--navy);margin:0 auto 14px}
.brand-name{font-family:"Lexend",sans-serif;font-weight:400;font-size:50px;color:var(--navy);line-height:1}
.brand-sub{font-family:"Lexend",sans-serif;font-weight:400;font-size:17px;letter-spacing:5px;color:var(--navy);margin-top:8px}

.over-tag{left:446px;top:48px;width:150px;height:36px;background:var(--royal);color:var(--white);font-family:"Lexend",sans-serif;font-size:33px;line-height:36px;padding-left:16px}
.big-number{left:572px;top:28px;font-family:"Lexend",sans-serif;font-weight:600;font-size:116px;line-height:1;color:var(--plum);letter-spacing:-3px}
.hours{left:443px;top:146px;font-family:"Lexend",sans-serif;font-weight:500;font-size:31px;line-height:1.13;color:var(--ink)}

.bar{background:var(--navy);height:15px;border-radius:0 40px 40px 0}
.bar-top{left:0;top:294px;width:442px}
.bar-bottom{left:0;top:572px;width:443px}
.band{left:0;top:310px;width:660px;height:261px;background:var(--green)}
.coach-name{left:51px;top:333px;font-family:"Lexend",sans-serif;font-weight:500;font-size:37px;color:var(--yellow)}
.coach-role{left:51px;top:375px;font-family:"Lexend",sans-serif;font-size:27px;color:var(--white)}
.bio{left:51px;top:418px;width:455px;font-size:12px;line-height:1.22;color:var(--white)}

.portrait{left:534px;top:211px}

.icon-badge{width:52px;height:52px;border-radius:50%;background:var(--plum);display:flex;align-items:center;justify-content:center}
.service-title{font-family:"Lexend",sans-serif;font-weight:500;font-size:29px;color:var(--navy);line-height:1.08}
.copy{font-size:17px;line-height:1.2}

.career-icon{left:51px;top:601px}
.career-title{left:115px;top:609px}
.career-a{left:51px;top:664px;width:432px}
.or-badge{left:57px;top:779px;width:34px;height:34px;border-radius:50%;background:var(--royal);color:var(--white);font-family:"Lexend",sans-serif;font-size:14px;line-height:34px;text-align:center}
.career-b{left:51px;top:828px;width:432px}

.callback-icon{left:557px;top:664px}
.callback-title{left:626px;top:660px}
.callback-copy{left:562px;top:733px;width:410px;font-size:16.5px}
.callback-copy p{margin-bottom:20px}

.navy-shape{left:0;top:948px}
.frac-icon{left:53px;top:977px;background:var(--white)}
.frac-title{left:115px;top:969px;color:var(--lime);font-size:30px;line-height:1}
.frac-copy{left:51px;top:1036px;width:930px;color:var(--white)}

.footer{left:51px;top:1129px;width:930px;display:flex;align-items:center;gap:18px;font-family:"Lexend",sans-serif}
.cta{font-size:17px;font-weight:500;color:var(--ink)}
.cta strong{color:var(--plum);font-weight:500}
.contact{display:flex;align-items:center;gap:8px;font-size:20px;color:var(--ink)}
</style>
</head>
<body>
<div class="flyer">

  <div class="abs brand">
    <div class="brand-dot"></div>
    <div class="brand-name">Quillmoor</div>
    <div class="brand-sub">COACHING</div>
  </div>

  <div class="abs over-tag">over</div>
  <div class="abs big-number">40,000</div>
  <div class="abs hours">HOURS OF LEADERSHIP &amp;<br>COACHING EXPERIENCE</div>

  <div class="abs bar bar-top"></div>
  <div class="abs band"></div>
  <div class="abs bar bar-bottom"></div>
  <div class="abs coach-name">Daniel Harrowgate</div>
  <div class="abs coach-role">YOUR PARTNER IN GROWTH</div>
  <p class="abs bio">Daniel Harrowgate brings over two decades of leadership experience across hospitality, culinary arts, and high-growth sales environments. That is over 40,000 hours of leadership and coaching experience. His career has been defined by a unique ability to build thriving teams, forge lasting relationships, and drive exceptional results in competitive markets. From award-winning kitchens to launching cannabis brands that became the fastest-growing in their state, Dan has consistently proven his talent for identifying potential and coaching others to achieve breakthrough performance.</p>

  <svg class="abs portrait" width="440" height="440" viewBox="0 0 440 440">
    <defs>
      <radialGradient id="photoTone" cx="50%" cy="45%" r="60%">
        <stop offset="0%" stop-color="#c9a58c"/>
        <stop offset="60%" stop-color="#7a6a62"/>
        <stop offset="100%" stop-color="#2e3440"/>
      </radialGradient>
    </defs>
    <circle cx="220" cy="220" r="205" fill="var(--white)" stroke="var(--green)" stroke-width="3"/>
    <circle cx="220" cy="220" r="172" fill="none" stroke="var(--purple)" stroke-width="18"/>
    <circle cx="220" cy="220" r="160" fill="url(#photoTone)" role="img" aria-label="Portrait photo of coach Daniel Harrowgate"/>
    <g fill="var(--white)" stroke="var(--purple)" stroke-width="2">
      <circle cx="293" cy="64" r="13"/>
      <circle cx="57" cy="164" r="13"/>
      <circle cx="381" cy="282" r="13"/>
      <circle cx="134" cy="369" r="13"/>
    </g>
  </svg>

  <div class="abs icon-badge career-icon">
    <svg width="30" height="30" viewBox="0 0 24 24" fill="none" stroke="#fff" stroke-width="1.8"><circle cx="8" cy="7" r="3"/><circle cx="16" cy="7" r="3"/><path d="M3 20c0-4 3-6 5-6s5 2 5 6M11 20c0-4 3-6 5-6s5 2 5 6"/></svg>
  </div>
  <div class="abs service-title career-title">CAREER COACHING</div>
  <p class="abs copy career-a">Sometimes the work isn't about your job—it's about you. I help leaders at all levels develop the confidence, communication skills, and clarity to show up as their best selves, both professionally and personally.</p>
  <div class="abs or-badge">OR</div>
  <p class="abs copy career-b">Thinking about a major career change? Feeling stuck and ready for something new? I guide professionals through pivotal transitions with the wisdom of someone who's made bold moves himself—and thrived.</p>

  <div class="abs icon-badge callback-icon">
    <svg width="30" height="30" viewBox="0 0 24 24" fill="none" stroke="#fff" stroke-width="1.8"><circle cx="10" cy="7" r="3.5"/><path d="M3 21c0-5 3-8 7-8"/><circle cx="17" cy="17" r="3"/><path d="M17 12v2M17 20v2M12 17h2M20 17h2"/></svg>
  </div>
  <div class="abs service-title callback-title">PROFESSIONAL STEADY<br>OAK CALLBACK</div>
  <div class="abs copy callback-copy">
    <p>Remember that friend who always seems to know what to say when you're stuck? That's what this is.</p>
    <p>Sometimes you don't need a six-month coaching program—<strong>you just need someone to talk through one specific challenge.</strong></p>
    <p>No long-term commitment. No pressure. Just honest conversation and the kind of guidance you'd get from someone who genuinely cares about seeing you succeed.</p>
  </div>

  <svg class="abs navy-shape" width="1017" height="164" viewBox="0 0 1017 164">
    <path d="M0 0 H455 C500 0 515 40 530 54 H1017 V164 H0 Z" fill="var(--navy)"/>
  </svg>
  <div class="abs icon-badge frac-icon">
    <svg width="32" height="32" viewBox="0 0 24 24" fill="none" stroke="var(--navy)" stroke-width="1.8"><circle cx="12" cy="12" r="4"/><path d="M12 10v4M11 11h2"/><circle cx="4.5" cy="5" r="2"/><circle cx="19.5" cy="5" r="2"/><circle cx="4.5" cy="19" r="2"/><circle cx="19.5" cy="19" r="2"/></svg>
  </div>
  <div class="abs service-title frac-title">FRACTIONAL<br>SALES LEADER</div>
  <p class="abs copy frac-copy">You don't need someone full time but you do want someone to coach, mentor, and drive your team. I can step in and help you get there in a fraction of the time at a fraction of the price of a full-time staff member.</p>

  <div class="abs footer">
    <div class="cta">SETUP A <strong>20-MINUTE CONSULTATION CALL</strong></div>
    <div class="contact">
      <svg width="26" height="26" viewBox="0 0 24 24"><circle cx="12" cy="12" r="11" fill="var(--green)"/><path d="M8.5 6.5l2 2-1.2 1.5c.8 1.7 2 2.9 3.7 3.7l1.5-1.2 2 2-1.3 1.6C11.5 16 8 12.5 7 8.2z" fill="#fff"/></svg>
      555-014-2290
    </div>
    <div class="contact">
      <svg width="26" height="26" viewBox="0 0 24 24" fill="none" stroke="var(--green)" stroke-width="1.8"><circle cx="12" cy="12" r="10"/><ellipse cx="12" cy="12" rx="4.5" ry="10"/><path d="M2 12h20M4 7h16M4 17h16"/></svg>
      quillmoorcoaching.com
    </div>
  </div>

</div>
</body>
</html>
```